eCommerce Landing Page Design for Wine Accessories using PageFly

Need to develop a landing page template that can be used for ecommerce products. This template needs to be built in PageFly (shopify App) if not in Pagefly, need an integrated app with shopify to maintain the correct url. The website is www.bluemarrowden.com. The template will be built using one product as an example. Copy and product images will be provided. the Landing page also must have "15% Off" and "free shipping" somewhere on the page

Although part of a website, I am open to different options on design

Target Market(s)

Wine drinkers

Requirements
Must have
• Built in PageFly (shopify App)
• Featured Product
• 15% Off
• Free Shipping
• High Converting with add to cart actions directly on the page

```html
<!DOCTYPE html>
<html lang="en">
<head>
<meta charset="utf-8">
<title>Blue Marrow Den — Insulated Wine Glasses</title>
<link rel="stylesheet" href="https://fonts.googleapis.com/css2?family=Montserrat:wght@500;600;700&family=Open+Sans:wght@400;600;700&display=swap">
<style>
:root{
  --red:#c4121f;
  --dark:#2f2f2f;
  --ink:#1c1c1c;
  --muted:#7a7a7a;
  --line:#dddddd;
  --promo-bg:#efedea;
  --blog-bg:#f3f3f3;
  --white:#ffffff;
}
*{box-sizing:border-box;margin:0;padding:0}
html,body{width:1200px;height:4852px;overflow:hidden;background:var(--white)}
body{position:relative;font-family:"Open Sans",Arial,sans-serif;color:var(--ink)}
.abs{position:absolute}
.topbar{left:0;top:0;width:1200px;height:28px;background:var(--dark);color:var(--white);font:700 10px/28px "Open Sans",sans-serif;letter-spacing:.8px;text-align:center}
.brand{left:38px;top:74px;display:flex;align-items:center;gap:8px;color:var(--red);font:700 22px/1 "Montserrat",sans-serif}
.brand-dot{width:14px;height:14px;border-radius:50%;background:var(--red)}
.nav{left:42px;top:152px;display:flex;gap:20px;font:700 10px "Open Sans",sans-serif;letter-spacing:.3px}
.nav .active{color:var(--red)}
.search{left:1082px;top:58px;width:98px;height:24px;display:flex;align-items:center;justify-content:space-between;font-size:9px;color:var(--muted);padding:0 4px}
.search .field{width:58px;height:18px;border-bottom:1px solid var(--line);line-height:18px}
.cart-link{left:1150px;top:126px;font:600 9px "Open Sans",sans-serif}
.hero{left:0;top:178px;width:1200px;height:540px;background:#f6f6f6}
.hero-photo{left:520px;top:178px;width:680px;height:540px;background:linear-gradient(150deg,#ffffff 0%,#f4f2f2 40%,#f5c25a 78%,#e8901c 100%)}
.hero-box{left:130px;top:333px;width:340px;height:191px;background:var(--white);border:1px solid var(--line);padding:34px 42px}
.hero-box h1{font:700 20px/1.25 "Montserrat",sans-serif;text-transform:uppercase;color:var(--ink)}
.btn{display:inline-block;background:var(--red);color:var(--white);font:700 11px/1 "Open Sans",sans-serif;text-transform:uppercase;letter-spacing:.5px;padding:9px 16px}
.hero-box .btn{margin-top:24px;padding:12px 20px;font-size:13px}
.section-title{left:0;width:1200px;text-align:center;font:700 18px "Montserrat",sans-serif;text-transform:uppercase}
.product{width:230px;text-align:center}
.product .shot{width:120px;height:245px;margin:0 auto;border-radius:60px 60px 10px 10px}
.product .name{margin-top:55px;font:600 11px/1.35 "Open Sans",sans-serif;text-transform:uppercase;height:34px}
.product .price{margin-top:6px;color:var(--red);font:700 18px "Open Sans",sans-serif}
.product .btn{margin-top:10px;padding:7px 10px;font-size:10px}
.banner-cell{top:1417px;width:400px;height:440px}
.banner-mid{left:400px;background:#222222;color:var(--white);text-align:center;padding-top:170px}
.banner-mid h2{font:600 17px "Montserrat",sans-serif;text-transform:uppercase}
.banner-mid .btn{margin-top:20px}
.latest{width:285px;text-align:center}
.latest .shot{height:339px}
.latest .name{margin-top:28px;font:600 11px "Open Sans",sans-serif;text-transform:uppercase}
.latest .price{margin-top:8px;color:var(--red);font:700 15px "Open Sans",sans-serif}
.promo{left:0;top:2548px;width:1200px;height:544px;background:var(--promo-bg)}
.promo-photo{left:133px;top:2626px;width:452px;height:375px;background:linear-gradient(120deg,#b91d23,#e0e0e0 40%,#8a7f93 65%,#4fc6a2)}
.promo-copy{left:663px;top:2664px;width:400px}
.promo-copy h2{font:700 21px/1.25 "Montserrat",sans-serif;text-transform:uppercase}
.promo-copy .off{margin-top:26px;color:var(--red);font:700 42px "Montserrat",sans-serif}
.promo-copy p{margin-top:18px;font:400 13px/1.55 "Open Sans",sans-serif;color:#333}
.promo-copy .btn{margin-top:24px}
.collection{width:295px}
.collection .shot{height:272px}
.collection .label{margin-top:20px;font:600 11px "Open Sans",sans-serif;text-transform:uppercase}
.blog{left:0;top:4049px;width:1200px;height:408px;background:var(--blog-bg)}
.blog-title{left:0;top:4108px;width:1200px;text-align:center;font:600 12px "Montserrat",sans-serif;letter-spacing:1.5px;text-transform:uppercase}
.post{top:4146px;width:312px;text-align:center}
.post .shot{height:204px}
.post .caption{margin-top:18px;font:400 11px/1.45 "Open Sans",sans-serif;color:#555}
.foot-col{top:4520px;width:300px;font:400 11px/1.75 "Open Sans",sans-serif;color:#333}
.foot-col h3{font:700 11px "Open Sans",sans-serif;text-transform:uppercase;margin-bottom:12px}
.subscribe-row{display:flex;margin-top:10px}
.subscribe-row .input{width:200px;height:28px;border:1px solid #cfcfcf;font-size:10px;line-height:26px;padding-left:10px;color:var(--muted);background:var(--white)}
.subscribe-row .btn{margin-left:10px;padding:8px 12px;font-size:10px}
.social{display:flex;gap:14px;margin-top:12px;font:600 10px "Open Sans",sans-serif}
.payments{left:0;top:4752px;width:1200px;display:flex;justify-content:center;gap:26px;font:700 12px "Open Sans",sans-serif;color:#444;letter-spacing:.5px}
.copyright{left:0;top:4800px;width:1200px;text-align:center;font:400 10px "Open Sans",sans-serif;color:#333}
</style>
</head>
<body>
<div class="abs topbar">FREE SHIPPING WORLDWIDE FOR ALL ORDERS</div>

<header>
  <div class="abs brand"><span class="brand-dot"></span>Blue Marrow Den</div>
  <nav class="abs nav"><span class="active">HOME</span><span>ABOUT US</span><span>COFFEE MUGS</span><span>SERVICES</span><span>BLOG</span><span>CONTACT US</span></nav>
  <div class="abs search"><span class="field">Find</span>
    <svg width="12" height="12" viewBox="0 0 12 12"><circle cx="5" cy="5" r="3.6" fill="none" stroke="#222" stroke-width="1.4"/><line x1="7.6" y1="7.6" x2="11" y2="11" stroke="#222" stroke-width="1.4"/></svg></div>
  <div class="abs cart-link">CART</div>
</header>

<section>
  <div class="abs hero"></div>
  <div class="abs hero-photo" role="img" aria-label="Purple, red and light blue stemmed insulated wine glasses over golden splashing wine"></div>
  <div class="abs hero-box">
    <h1>New 10oz Stainless Double Wall Insulated Wine Glass</h1>
    <span class="btn">Shop now</span>
  </div>
</section>

<section>
  <h2 class="abs section-title" style="top:798px">Featured Product</h2>
  <div class="abs product" style="left:98px;top:905px">
    <div class="shot" role="img" aria-label="Red stemmed tumbler" style="background:linear-gradient(#d01c24,#a5121a)"></div>
    <div class="name">Day Drinking Tumbler</div><div class="price">$32.95</div><span class="btn">Add to cart</span>
  </div>
  <div class="abs product" style="left:364px;top:905px">
    <div class="shot" role="img" aria-label="Light blue stainless margarita glass" style="background:linear-gradient(#a8c3e0,#7ea2c8)"></div>
    <div class="name">Stainless Steel<br>Margarita Glass</div><div class="price">$16.95</div><span class="btn">Add to cart</span>
  </div>
  <div class="abs product" style="left:639px;top:905px">
    <div class="shot" role="img" aria-label="Purple stainless martini glass" style="background:linear-gradient(#a23aa6,#7a2280)"></div>
    <div class="name">Stainless Stee<br>L Martini Glass</div><div class="price">$16.95</div><span class="btn">Add to cart</span>
  </div>
  <div class="abs product" style="left:900px;top:905px">
    <div class="shot" role="img" aria-label="Lime green beer glass" style="background:linear-gradient(#9ec435,#6f9a1c)"></div>
    <div class="name">Flip Beer Double<br>Layer Glass</div><div class="price">$20.97</div><span class="btn">Add to cart</span>
  </div>
</section>

<section>
  <div class="abs banner-cell" style="left:0" role="img" aria-label="Row of colourful insulated wine glasses on a wooden table" ></div>
  <div class="abs banner-cell" style="left:0;background:linear-gradient(120deg,#c9b9a4,#d9d5d2 45%,#9a8fa6 70%,#6ccfb0)"></div>
  <div class="abs banner-cell banner-mid"><h2>Fine Crystal Wine Glass</h2><span class="btn">Shop now</span></div>
  <div class="abs banner-cell" style="left:800px;background:linear-gradient(120deg,#e8dccb,#a14aa8 55%,#e9e2d8)" role="img" aria-label="Purple wine glass on a table by a window"></div>
</section>

<section>
  <h2 class="abs section-title" style="top:1950px">Latest Products</h2>
  <div class="abs latest" style="left:133px;top:2054px">
    <div class="shot" role="img" aria-label="Silver wine glass on a checked cloth" style="background:linear-gradient(#e8e8e8,#b8b8b8)"></div>
    <div class="name">Water Inductive LED Glass</div><div class="price">$5.97</div>
  </div>
  <div class="abs latest" style="left:456px;top:2054px">
    <div class="shot" role="img" aria-label="Pink wine cup" style="background:linear-gradient(#f1e6e6,#c53b86)"></div>
    <div class="name">Creative Wine Cup</div><div class="price">$70.97</div>
  </div>
  <div class="abs latest" style="left:779px;top:2054px">
    <div class="shot" role="img" aria-label="Mint green wine glass" style="background:linear-gradient(#eef0ef,#4fc6a2)"></div>
    <div class="name">Wine Holder for 2 Wine Glasses &amp; Bottle</div><div class="price">$26.97</div>
  </div>
</section>

<section>
  <div class="abs promo"></div>
  <div class="abs promo-photo" role="img" aria-label="Red, white, silver, purple and mint insulated wine glasses"></div>
  <div class="abs promo-copy">
    <h2>New 10oz Stainless Double Wall Insulated Wine Glass</h2>
    <div class="off">15% OFF</div>
    <p>We're so sure that you will love our products here at Blue Marrow Den and offer our 100% satisfaction guarantee. If you have a problem with your order and no one else can help, send us an email over to sales@bluemarrowden.com and we'll do our Blue Marrow Den guarantee best to make things right for you.</p>
    <span class="btn">Shop now</span>
  </div>
</section>

<section>
  <h2 class="abs section-title" style="top:3179px">Our Collections</h2>
  <div class="abs collection" style="left:133px;top:3266px"><div class="shot" role="img" aria-label="Assorted insulated wine glasses" style="background:linear-gradient(120deg,#c21e25,#dedede 45%,#8b4a94 70%,#4fc6a2)"></div><div class="label">Stainless Double Wall Insulated Wine Glass</div></div>
  <div class="abs collection" style="left:453px;top:3266px"><div class="shot" role="img" aria-label="White wine glass" style="background:linear-gradient(#f2efea,#d8d5d0)"></div><div class="label">Wine Bottle Shaped Ice Cube Cooler</div></div>
  <div class="abs collection" style="left:773px;top:3266px"><div class="shot" role="img" aria-label="Light blue wine glass" style="background:linear-gradient(#eee8e2,#9ab7d8)"></div><div class="label">Lead-Free Crystal Glass</div></div>
  <div class="abs collection" style="left:133px;top:3625px"><div class="shot" role="img" aria-label="Magenta wine glass" style="background:linear-gradient(#efe8e4,#c0236f)"></div><div class="label">Stainless Double Wall Insulated Wine Glass</div></div>
  <div class="abs collection" style="left:453px;top:3625px"><div class="shot" role="img" aria-label="Lime green wine glass" style="background:linear-gradient(#efebe4,#8fbb2c)"></div><div class="label">Walled Stainless Steel Beer Mug</div></div>
  <div class="abs collection" style="left:773px;top:3625px"><div class="shot" role="img" aria-label="Red wine glass" style="background:linear-gradient(#efe9e3,#c4161f)"></div><div class="label">Survive Tumbler</div></div>
</section>

<section>
  <div class="abs blog"></div>
  <h2 class="abs blog-title">Blog</h2>
  <div class="abs post" style="left:120px"><div class="shot" role="img" aria-label="Silver wine glass" style="background:linear-gradient(#efefef,#bdbdbd)"></div><div class="caption">Ice cream brunch roundup: Our verdict</div></div>
  <div class="abs post" style="left:453px"><div class="shot" role="img" aria-label="Black poster with white love lettering" style="background:#111"></div><div class="caption">NEW! Mr. Bellamy's ice cream available for same day delivery</div></div>
  <div class="abs post" style="left:779px"><div class="shot" role="img" aria-label="Colourful wine glasses" style="background:linear-gradient(120deg,#c21e25,#dcdcdc 45%,#8b4a94)"></div><div class="caption">Vinefield Cookbook: Illustrated recipes from artists around the world</div></div>
</section>

<footer>
  <div class="abs foot-col" style="left:133px"><h3>Menu</h3>Home<br>Categories<br>Blog<br>Contact Us</div>
  <div class="abs foot-col" style="left:488px"><h3>Info</h3>My Account<br>Login<br>My cart<br>Register</div>
  <div class="abs foot-col" style="left:815px"><h3>Subscribe</h3>Sign up to our mailing list
    <div class="subscribe-row"><span class="input">E-mail id</span><span class="btn">OK</span></div>
    <div class="social"><span>Friendly</span><span>Chirp</span><span>Snapframe</span><span>Reelio</span></div>
  </div>
  <div class="abs payments"><span>CARDLY</span><span>ORBIS</span><span>TRAVELA</span><span>PAYWELL</span><span>DINEPASS</span><span>FARPAY</span></div>
  <div class="abs copyright">Copyrights © 2018 All Rights Reserved</div>
</footer>
</body>
</html>
```